Mockup design for a fashion contest website

The website is a landing page for a fashion contest. Participants are fashion students, designers, merchandisers, stylists, and other fashion enthusiasts. Website should have a clean, modern look and should be "headline-y" in nature. Website should be very visual with good use of images since the audience is fashion (specifically women's clothing). Contestants will earn points by identifying fashion/clothing items within images.

Here's what I am thinking:

Title:
Fashion Contest by Vendrift

Headlines (each with subheadline of 10-15 words )
Can you find the features in the image?
This will be a carousel showing 3-4 images with callouts
Have callouts for each of the categories like this: https://img.examplecdn.test/v/9QwzLm/preview.jpg
Broad categories for items are labeled like:
Top
Dress
Jeans
Pants
Shorts
Blouse
Skirt
Standard
Crop Top
Shirt
Sweater
Detail fashion attributes are in the spreadsheet attached

Earn Points
and see where you stand -- leaderboard graphic
Win Prizes
Need a way to show multiple prizes here:
Grand prizes: Tablo Max, Halvex Lumora QZ-870T Wi-Fi Digital Camera, Stitchwell KR5530TN Sewing Machine, Drafty Linea Max Drawing tablet
Other prizes: Orvane Earlets, Gift cards to great stores: Mivo, Lumo, Blushery, etc.

What You Need To Know
How to Enter (25-30 words)
How do I qualify? (10-15 words)
What are the contest dates (10-15 words)
What is this for? (10-15 words)

----

Tell Your Friends (10 words) [Needs to be shown more prominently as we will have referral bonuses]

The Legal Stuff / Terms & Conditions
[Each subsection 50 words]
Eligibility
Winners & Prizes
Privacy Policy
Judging
Disclaimer

Other sections (shown as links on top perhaps)
Blog - standard blog format. No need for design
Forum - use threadloom software. No need for design
Standings
FAQ
Contact - link to email - no need for design

Need to have clear CTA to sign up on bottom.

Need to Design ‘Standings’ Page:

Show Leaderboard
Ranking, Username, total points, change in ranking (up or down)

Show Total number of images processed. This can be progress bar like in crowdfunding sites:
https://snapbin.test/kTrvo/58ac91d3e0.png
It would say:
300,000 images processed by 1,000 participants
x% of 1,000,000 goal a month left

Goals and Stretch Goals for the Contest

500,000 images
Grand prizes (1 winner)
Other prizes (3 winners)

1,000,000 images
Grand prizes (2 winners)
Other prizes (6 winners)

2,000,000 images
Grand prizes (3 winners)
Other prizes (9 winners)

3,000,000 images
Grand prizes (4 winners)
Other prizes (12 winners)

How to Earn Points

Points awarded for correctly completing task
Points are deducted for making mistakes and unnecessary skips

Help
just a click away. Post a message on the community forum and ask a question.
----
High contrasty (black & white) with one color perhaps blue should be color palette. Look at our logo for design motif ideas.
Updates

Target Market(s)

Fashion community

Industry/Entity Type

Fashion

Number of Pages Required

2 page

Font styles to use
Sans Serif

Requirements
Must have
• one page scroll website (the quiz is a separate page though)
• beautiful graphics and images
• placeholder text where number of words is written
Nice to have
• written copy ideas
Should not have
• the vendrift logo should not be prominently featured. the emphasis is on 'Fashion Contest'

```html
<!DOCTYPE html>
<html lang="en">
<head>
<meta charset="utf-8">
<title>Fashion Contest by Vendrift</title>
<link href="https://fonts.googleapis.com/css2?family=Roboto+Slab:wght@400;500&family=Raleway:wght@400;500;600&family=Open+Sans:wght@400;600&display=swap" rel="stylesheet">
<style>
:root{
  --navy:#0c1a55;
  --navy-deep:#081244;
  --navy-soft:#4d5a8a;
  --ink:#1b1f33;
  --muted:#5b5f6e;
  --line:#d7d9e0;
  --paper:#ffffff;
  --mist:#eef0f3;
  --violet:#b845e8;
  --indigo:#3b2f9a;
}
*{box-sizing:border-box;margin:0;padding:0}
html,body{width:1200px;height:2423px;overflow:hidden;background:var(--paper)}
body{position:relative;font-family:"Open Sans",Arial,sans-serif;color:var(--ink)}
.abs{position:absolute}
h1,h2,h3,h4{font-family:"Roboto Slab",Georgia,serif;font-weight:400;color:var(--navy)}
.section-title{position:absolute;left:0;width:1200px;text-align:center;font-size:23px}
.section-sub{position:absolute;left:0;width:1200px;text-align:center;font-size:10px;color:var(--muted)}
.btn{position:absolute;background:var(--navy);color:#fff;border-radius:20px;font-family:"Raleway",Arial,sans-serif;font-size:13px;display:flex;align-items:center;justify-content:center}

/* header */
.site-header{left:0;top:0;width:1200px;height:44px;background:#fff}
.brand{left:249px;top:9px;display:flex;align-items:center;gap:8px;font-family:"Raleway",Arial,sans-serif;font-size:24px;font-weight:500;color:var(--navy-deep);letter-spacing:1px}
.brand-mark{width:20px;height:20px;background:var(--navy-deep)}
.main-nav{left:610px;top:13px;width:250px;display:flex;justify-content:space-between;font-family:"Raleway",Arial,sans-serif;font-size:9.5px;align-items:center;white-space:nowrap}
.main-nav .current{background:var(--navy);color:#fff;padding:3px 8px;border-radius:10px}
.social{left:887px;top:17px;display:flex;gap:12px;align-items:center}
.social span{width:7px;height:7px;border-radius:50%;background:var(--navy-deep)}

/* hero */
.hero{left:0;top:44px;width:1200px;height:432px;background:radial-gradient(ellipse 45% 60% at 24% 38%,#f6f6f6 0%,#e2e1df 45%,rgba(226,225,223,0) 100%),linear-gradient(90deg,#9a9896 0%,#c8c6c3 30%,#8a7f78 55%,#2c2624 70%,#6b5a4a 85%,#2b2726 100%);border-bottom:2px solid var(--navy)}
.hero-title{left:249px;top:200px;font-size:22px}
.hero-rule{left:249px;top:236px;width:245px;height:1px;background:var(--navy)}
.hero-text{left:249px;top:245px;width:300px;font-size:9px;line-height:13px;color:#333}

/* categories + carousel */
.categories{left:249px;top:567px;width:187px;height:281px;border:1px solid var(--line)}
.categories-head{background:var(--navy);color:#fff;text-align:center;height:42px;padding-top:4px}
.categories-head h3{color:#fff;font-size:15px}
.categories-head p{font-size:8px}
.categories ul{list-style:none}
.categories li{height:21.6px;line-height:21.6px;padding-left:9px;font-size:10px;border-bottom:1px solid var(--line);color:#444}
.categories li.active{background:var(--navy);color:#fff}
.carousel-stage{left:454px;top:567px;width:496px;height:203px;border:1px solid var(--navy);background:linear-gradient(100deg,#e9ebee 0%,#d5d8dd 30%,#6d7fa6 55%,#9fb0cc 70%,#e2e4e8 100%)}
.caption{left:464px;top:685px;width:205px;height:36px;background:var(--navy);color:#fff;padding:3px 14px}
.caption small{font-size:8px;display:block}
.caption strong{font-family:"Roboto Slab",Georgia,serif;font-weight:400;font-size:13px}
.arrows{left:675px;top:747px;display:flex;gap:2px}
.arrows span{width:24px;height:22px;background:var(--navy);display:flex;align-items:center;justify-content:center}
.thumb{top:780px;width:161px;height:68px;border:1px solid var(--line)}
.thumb.active{border:2px solid var(--navy)}

/* earn points */
.points{left:0;top:866px;width:1200px;height:248px;background:radial-gradient(ellipse at 50% 50%,#fafafa 30%,#e4e4e4 100%)}
.board{left:375px;top:942px;width:497px}
.board-row{height:22px;margin-bottom:2.2px;display:flex;align-items:center;color:#fff;font-size:9px;padding:0 10px;position:relative}
.board-row .name{width:210px}
.board-row .stars{letter-spacing:1px;font-size:10px}
.board-row .pct{position:absolute;right:10px;color:#e6e8f0}

/* win prizes */
.prizes{left:0;top:1114px;width:1200px;height:302px;background:linear-gradient(90deg,var(--violet) 0%,#7b4bd8 30%,var(--indigo) 60%,#1d1e66 100%);border-top:2px solid var(--navy)}
.prize{left:250px;width:335px;height:55px;display:flex;box-shadow:0 0 12px rgba(255,255,255,.5)}
.prize-body{flex:1;background:#fff;padding:3px 6px}
.prize-body h4{font-size:13px;color:var(--navy)}
.prize-body p{font-size:8px;line-height:11px;color:#333}
.prize-icon{width:46px;background:var(--navy);display:flex;align-items:center;justify-content:center}
.gift-visual{left:735px;top:1205px;width:175px;height:180px;border-radius:8px;background:radial-gradient(circle,rgba(255,255,255,.22),rgba(255,255,255,0) 70%)}

/* need to know */
.know-item{top:1520px;width:175px;text-align:center}
.know-item svg{display:block;margin:0 auto}
.know-item h4{font-size:12px;margin-top:8px;color:var(--navy)}
.know-item p{font-size:8.5px;line-height:13px;color:#444;margin-top:3px}

/* tell friends */
.tell{left:0;top:1626px;width:1200px;height:159px;background:var(--navy-deep)}
.tell-photo{left:565px;top:1626px;width:440px;height:159px;background:linear-gradient(90deg,rgba(8,18,68,1) 0%,#6b5d66 25%,#b9a59a 50%,#8c7d80 75%,rgba(8,18,68,1) 100%)}
.tell-pill{left:-20px;top:1683px;width:500px;height:47px;border:1px solid #c8cde0;border-radius:0 24px 24px 0}
.tell-pill h3{position:absolute;left:269px;top:3px;color:#fff;font-size:17px}
.tell-pill p{position:absolute;left:269px;top:27px;color:#e3e6f0;font-size:9px;white-space:nowrap}
.tell-pill svg{position:absolute;right:-10px;top:15px;background:var(--navy-deep)}

/* legal */
.legal{left:0;top:1785px;width:1200px;height:239px;background:linear-gradient(90deg,#8e8c8b 0%,#c9c6c2 20%,#4d4645 35%,#d9dadc 55%,#e9eaec 100%)}
.legal-title{left:644px;top:1815px;font-size:17px}
.legal-list{left:656px;top:1852px;list-style:none}
.legal-list li{height:31.5px}
.legal-list strong{font-family:"Roboto Slab",Georgia,serif;font-weight:400;font-size:11px;color:var(--navy);display:flex;align-items:center;gap:5px}
.legal-list span{display:block;padding-left:13px;font-size:8.5px;color:#333}

/* blog */
.post{top:2104px;width:191px;height:257px;border:1px solid var(--line);box-shadow:0 1px 3px rgba(0,0,0,.1)}
.post-photo{height:89px}
.post h4{font-size:12px;color:#111;margin:14px 0 0 7px}
.post time{display:block;text-align:center;font-size:6.5px;color:#444}
.post p{font-size:9px;line-height:13.5px;color:#333;margin:4px 7px 0}
.post .btn{left:38px;top:216px;width:115px;height:28px}

/* footer */
.footer-line{left:0;top:2398px;width:1200px;height:2px;background:var(--navy)}
.copyright{left:249px;top:2404px;font-size:8.5px;color:#333}
.footer-nav{left:711px;top:2404px;display:flex;gap:17px;font-size:8.5px;color:#333}
</style>
</head>
<body>

<header class="site-header abs">
  <div class="brand abs"><span class="brand-mark"></span>VENDRIFT</div>
  <nav class="main-nav abs">
    <span class="current">Home</span><span>Forum</span><span>Standings</span><span>FAQ</span><span>Blog</span><span>Contact</span>
  </nav>
  <div class="social abs"><span></span><span></span><span></span>
    <svg width="9" height="9" viewBox="0 0 10 10"><circle cx="4" cy="4" r="3" fill="none" stroke="#081244" stroke-width="1.6"/><line x1="6.2" y1="6.2" x2="9.5" y2="9.5" stroke="#081244" stroke-width="1.6"/></svg>
  </div>
</header>

<section class="hero abs" role="img" aria-label="Runway photograph of models in sunglasses and fur jackets"></section>
<h1 class="hero-title abs">Fashion Contest by Vendrift</h1>
<div class="hero-rule abs"></div>
<p class="hero-text abs">Lorem Ipsum is simply dummy text of the printing and typesetting industry. Lorem Ipsum has been the industry's standard dummy</p>
<div class="btn" style="left:249px;top:282px;width:150px;height:32px;font-size:14px">Apply Now</div>

<h2 class="section-title" style="top:497px">Fashion Contest by Vendrift</h2>
<p class="section-sub" style="top:532px">Lorem Ipsum is simply dummy text of the printing and typesetting industry</p>

<aside class="categories abs">
  <div class="categories-head"><h3>Categories</h3><p>Broad categories for items are labeled like:</p></div>
  <ul>
    <li>Top</li><li>Dress</li><li class="active">Jeans</li><li>Pants</li><li>Shorts</li><li>Blouse</li><li>Skirt</li><li>Standard</li><li>Crop Top</li><li>Shirt</li><li>Sweater</li>
  </ul>
</aside>
<div class="carousel-stage abs" role="img" aria-label="Close-up photograph of ripped blue jeans and a leather jacket"></div>
<div class="caption abs"><small>Design by</small><strong>Stella Marwood</strong></div>
<div class="arrows abs">
  <span><svg width="8" height="8" viewBox="0 0 8 8"><path d="M5.5 1 2.5 4l3 3" fill="none" stroke="#fff" stroke-width="1.5"/></svg></span>
  <span><svg width="8" height="8" viewBox="0 0 8 8"><path d="M2.5 1l3 3-3 3" fill="none" stroke="#fff" stroke-width="1.5"/></svg></span>
</div>
<div class="thumb abs" style="left:454px;background:linear-gradient(90deg,#b7b4b1,#6b5a4c,#cfcdca)" role="img" aria-label="Thumbnail of a model with a brown handbag"></div>
<div class="thumb abs" style="left:622px;background:linear-gradient(90deg,#cfc6b9,#45506e,#b5a894)" role="img" aria-label="Thumbnail of jeans with a belt"></div>
<div class="thumb abs active" style="left:790px;background:linear-gradient(90deg,#e4e5e8,#7d8fb3,#dfe1e5)" role="img" aria-label="Thumbnail of ripped jeans"></div>

<section class="points abs"></section>
<h2 class="section-title" style="top:882px">Earn Points</h2>
<p class="section-sub" style="top:912px">Lorem Ipsum is simply dummy text of the printing</p>
<div class="board abs">
  <div class="board-row" style="background:linear-gradient(115deg,var(--navy) 88%,var(--navy-soft) 88%)"><span class="name">Jorel Asteria</span><span class="stars">★★★★½</span><span class="pct">90%</span></div>
  <div class="board-row" style="background:linear-gradient(115deg,var(--navy) 79%,var(--navy-soft) 79%)"><span class="name">Adina Varel</span><span class="stars">★★★½</span><span class="pct">80%</span></div>
  <div class="board-row" style="background:linear-gradient(115deg,var(--navy) 74%,var(--navy-soft) 74%)"><span class="name">Piet Ravelle</span><span class="stars">★★★½</span><span class="pct">75%</span></div>
  <div class="board-row" style="background:linear-gradient(115deg,var(--navy) 60%,var(--navy-soft) 60%)"><span class="name">Piers Cadrell</span><span class="stars">★★★</span><span class="pct">60%</span></div>
  <div class="board-row" style="background:linear-gradient(115deg,var(--navy) 57%,var(--navy-soft) 57%)"><span class="name">Coralie Vane</span><span class="stars">★★★</span><span class="pct">61%</span></div>
  <div class="board-row" style="background:linear-gradient(115deg,var(--navy) 54%,var(--navy-soft) 54%)"><span class="name">Lisette Charvel</span><span class="stars">★★½</span><span class="pct">59%</span></div>
</div>

<section class="prizes abs"></section>
<h2 class="section-title" style="top:1139px;color:#fff">Win Prizes</h2>
<p class="section-sub" style="top:1172px;color:#ecebff">Lorem Ipsum is simply dummy text of the</p>
<div class="prize abs" style="top:1213px">
  <div class="prize-body"><h4>Grand prizes</h4><p>Tablo Max, Halvex Lumora QZ-870T Wi-Fi Digital Camera, Stitchwell KR5530TN Sewing Machine, Drafty Linea Max Drawing tablet</p></div>
  <div class="prize-icon"><svg width="22" height="22" viewBox="0 0 22 22" fill="none" stroke="#fff" stroke-width="1.4"><rect x="3" y="8" width="16" height="4"/><rect x="4.5" y="12" width="13" height="8"/><line x1="11" y1="8" x2="11" y2="20"/><path d="M11 8C9 4 5 4 6 7M11 8c2-4 6-4 5-1"/></svg></div>
</div>
<div class="prize abs" style="top:1273px">
  <div class="prize-body"><h4>Winner prizes</h4><p>Tablo Max, Halvex Lumora QZ-870T Wi-Fi Digital Camera, Stitchwell KR5530TN Sewing Machine, Drafty Linea Max Drawing tablet</p></div>
  <div class="prize-icon"><svg width="22" height="22" viewBox="0 0 22 22" fill="none" stroke="#fff" stroke-width="1.4"><rect x="3" y="8" width="16" height="4"/><rect x="4.5" y="12" width="13" height="8"/><line x1="11" y1="8" x2="11" y2="20"/><path d="M11 8C9 4 5 4 6 7M11 8c2-4 6-4 5-1"/></svg></div>
</div>
<div class="prize abs" style="top:1332px">
  <div class="prize-body"><h4>Other prizes</h4><p>Tablo Max, Halvex Lumora QZ-870T Wi-Fi Digital Camera, Stitchwell KR5530TN Sewing Machine, Drafty Linea Max Drawing tablet</p></div>
  <div class="prize-icon"><svg width="22" height="22" viewBox="0 0 22 22" fill="none" stroke="#fff" stroke-width="1.4"><rect x="3" y="8" width="16" height="4"/><rect x="4.5" y="12" width="13" height="8"/><line x1="11" y1="8" x2="11" y2="20"/><path d="M11 8C9 4 5 4 6 7M11 8c2-4 6-4 5-1"/></svg></div>
</div>
<div class="gift-visual abs" role="img" aria-label="Line illustration of an open gift box with confetti"></div>

<h2 class="section-title" style="top:1439px">What You Need To Know</h2>
<p class="section-sub" style="top:1473px">Lorem Ipsum is simply dummy text of the printing and typesetting</p>
<div class="know-item abs" style="left:242px">
  <svg width="30" height="30" viewBox="0 0 30 30" fill="none" stroke="#0c1a55" stroke-width="1.5"><rect x="9" y="3" width="14" height="24"/><path d="M3 15h12M11 11l4 4-4 4"/></svg>
  <h4>How to Enter</h4><p>Lorem Ipsum is simply dummy text of the printing and</p>
</div>
<div class="know-item abs" style="left:423px">
  <svg width="30" height="30" viewBox="0 0 30 30" fill="none" stroke="#0c1a55" stroke-width="1.5"><path d="M8 3h10l5 5v19H8z"/><path d="M11 13h9M11 17h9M11 21h9"/></svg>
  <h4>How do I qualify?</h4><p>Lorem Ipsum is simply dummy text of the printing and</p>
</div>
<div class="know-item abs" style="left:604px">
  <svg width="30" height="30" viewBox="0 0 30 30" fill="none" stroke="#0c1a55" stroke-width="1.5"><rect x="4" y="5" width="22" height="21"/><path d="M4 10h22M10 3v4M20 3v4"/><text x="15" y="23" text-anchor="middle" font-size="10" fill="#0c1a55" stroke="none" font-family="Arial,sans-serif">19</text></svg>
  <h4>What are the contest dates</h4><p>Lorem Ipsum is simply dummy text of the printing and</p>
</div>
<div class="know-item abs" style="left:785px">
  <svg width="30" height="30" viewBox="0 0 30 30"><text x="15" y="23" text-anchor="middle" font-size="18" fill="#0c1a55" font-family="Arial,sans-serif">?</text></svg>
  <h4>What is this for</h4><p>Lorem Ipsum is simply dummy text of the printing and</p>
</div>

<section class="tell abs"></section>
<div class="tell-photo abs" role="img" aria-label="Photograph of models walking a runway in sequined dresses"></div>
<div class="tell-pill abs">
  <h3>Tell Your Friends</h3>
  <p>Lorem Ipsum is simply dummy text of the printing</p>
  <svg width="20" height="16" viewBox="0 0 20 16" fill="none" stroke="#fff" stroke-width="1.3"><rect x="2" y="2" width="16" height="12"/><path d="M2 2l8 7 8-7"/></svg>
</div>

<section class="legal abs" role="img" aria-label="Blurred runway photograph of models in sunglasses"></section>
<h3 class="legal-title abs">The Legal Stuff / Terms &amp; Conditions</h3>
<ul class="legal-list abs">
  <li><strong><svg width="8" height="8" viewBox="0 0 8 8"><rect x=".5" y=".5" width="7" height="7" fill="none" stroke="#0c1a55"/><path d="M2 4l1.5 1.5L6 2.5" fill="none" stroke="#0c1a55"/></svg>Eligibility</strong><span>Lorem Ipsum is simply dummy text of the printing been</span></li>
  <li><strong><svg width="8" height="8" viewBox="0 0 8 8"><rect x=".5" y=".5" width="7" height="7" fill="none" stroke="#0c1a55"/><path d="M2 4l1.5 1.5L6 2.5" fill="none" stroke="#0c1a55"/></svg>Winners &amp; Prizes</strong><span>Lorem Ipsum is simply dummy text of the printing been</span></li>
  <li><strong><svg width="8" height="8" viewBox="0 0 8 8"><rect x=".5" y=".5" width="7" height="7" fill="none" stroke="#0c1a55"/><path d="M2 4l1.5 1.5L6 2.5" fill="none" stroke="#0c1a55"/></svg>Privacy Policy</strong><span>Lorem Ipsum is simply dummy text of the printing been</span></li>
  <li><strong><svg width="8" height="8" viewBox="0 0 8 8"><rect x=".5" y=".5" width="7" height="7" fill="none" stroke="#0c1a55"/><path d="M2 4l1.5 1.5L6 2.5" fill="none" stroke="#0c1a55"/></svg>Judging</strong><span>Lorem Ipsum is simply dummy text of the printing been</span></li>
  <li><strong><svg width="8" height="8" viewBox="0 0 8 8"><rect x=".5" y=".5" width="7" height="7" fill="none" stroke="#0c1a55"/><path d="M2 4l1.5 1.5L6 2.5" fill="none" stroke="#0c1a55"/></svg>Disclaimer</strong><span>Lorem Ipsum is simply dummy text of the printing been</span></li>
</ul>

<h2 class="section-title" style="top:2044px">Our Blog</h2>
<p class="section-sub" style="top:2077px">Lorem Ipsum is simply dummy text of the</p>
<article class="post abs" style="left:281px">
  <div class="post-photo" role="img" aria-label="Photograph of a woman in sunglasses" style="background:linear-gradient(90deg,#f1ece4,#c49a6c,#e8e4de)"></div>
  <h4>Introduction</h4><time>7 - feb - 2017</time>
  <p>Lorem Ipsum is simply dummy text of the printing and typesetting industry. Lorem Ipsum has been the industry's standard dummy text ever since the 1500s, when an unknown printer</p>
  <div class="btn">Read More</div>
</article>
<article class="post abs" style="left:500px">
  <div class="post-photo" role="img" aria-label="Photograph of a woman in a scarf and sunglasses" style="background:linear-gradient(90deg,#d9cfc2,#5a4a40,#d6ccc0)"></div>
  <h4>Introduction</h4><time>7 - feb - 2017</time>
  <p>Lorem Ipsum is simply dummy text of the printing and typesetting industry. Lorem Ipsum has been the industry's standard dummy text ever since the 1500s, when an unknown printer</p>
  <div class="btn">Read More</div>
</article>
<article class="post abs" style="left:719px">
  <div class="post-photo" role="img" aria-label="Photograph of a woman walking by a railing" style="background:linear-gradient(90deg,#d2d4d6,#a9abae,#e1e2e4)"></div>
  <h4>Introduction</h4><time>7 - feb - 2017</time>
  <p>Lorem Ipsum is simply dummy text of the printing and typesetting industry. Lorem Ipsum has been the industry's standard dummy text ever since the 1500s, when an unknown printer</p>
  <div class="btn">Read More</div>
</article>

<footer>
  <div class="footer-line abs"></div>
  <div class="btn" style="left:538px;top:2379px;width:124px;height:35px;font-size:15px">Sign Up</div>
  <p class="copyright abs">© 2009 - 2017 vendrift.com</p>
  <nav class="footer-nav abs"><span>Home</span><span>Forum</span><span>Standings</span><span>FAQ</span><span>Blog</span><span>Contact</span></nav>
</footer>

</body>
</html>
```